Bref créative
Stationery design for KORV Holdings
KORV Holdings - Motion Lessons & Media
Use same font as used in my logo
Trajan Bold
Bright & Fun-filled
Damian Whitcombe
IT & Technical Support
The Lumley House
12 Fenwick Lane
Ashcombe-Under-Lyne
Bristol
BS4 7QD
damian@korv.co
www.korv.co
This is the KORV Holdings logo.

```html
<!DOCTYPE html>
<html lang="en">
<head>
<meta charset="utf-8">
<title>KORV Holdings – Business Card</title>
<link rel="stylesheet" href="https://fonts.googleapis.com/css2?family=Cinzel:wght@700&family=Open+Sans:wght@400;600;700&display=swap">
<style>
  :root {
    --backdrop: #e4e4e4;
    --card-white: #fbfbfb;
    --card-black: #0d0d0d;
    --gold-light: #d8b45a;
    --gold: #b08a2e;
    --gold-dark: #7a5c14;
    --ink: #4a4a4a;
    --white: #ffffff;
  }
  * { margin: 0; padding: 0; box-sizing: border-box; }
  html, body { width: 1200px; height: 901px; overflow: hidden; }
  body {
    background: var(--backdrop);
    font-family: "Open Sans", Arial, sans-serif;
    position: relative;
  }
  .card {
    position: absolute;
    left: 260px;
    width: 680px;
    height: 389px;
    border-radius: 22px;
    overflow: hidden;
    box-shadow: 0 6px 18px rgba(0,0,0,0.18);
  }
  .card--back { top: 41px; background: var(--card-black); }
  .card--front { top: 470px; background: var(--card-white); }
  .card__band { position: absolute; inset: 0; }
  .wordmark {
    position: absolute;
    font-family: "Cinzel", "Trajan Pro", serif;
    font-weight: 700;
    color: var(--gold);
    white-space: nowrap;
    letter-spacing: 2px;
  }
  .card--back .wordmark {
    left: 0; right: 0; top: 165px;
    text-align: center;
    font-size: 50px;
    color: var(--gold-light);
  }
  .card--front .wordmark {
    left: 110px; top: 40px;
    font-size: 44px;
  }
  .holder {
    position: absolute;
    left: 110px; top: 118px;
  }
  .holder__name {
    font-weight: 700;
    font-size: 18px;
    color: var(--gold);
  }
  .holder__role {
    font-size: 13px;
    color: var(--ink);
    margin-top: 2px;
  }
  .contact {
    position: absolute;
    right: 40px; top: 198px;
    color: var(--white);
    font-size: 12.5px;
    line-height: 17px;
    letter-spacing: 0.6px;
  }
  .contact__address { margin-bottom: 10px; }
  .contact__row { display: flex; align-items: center; gap: 7px; }
  .contact__row svg { width: 12px; height: 12px; flex: none; }
</style>
</head>
<body>

<section class="card card--back" aria-label="Card back">
  <div class="wordmark">KORV Holdings</div>
</section>

<section class="card card--front" aria-label="Card front">
  <svg class="card__band" viewBox="0 0 680 389" preserveAspectRatio="none" role="img" aria-label="Gold band across the lower part of the card">
    <defs>
      <linearGradient id="goldBand" x1="0" y1="0" x2="1" y2="1">
        <stop offset="0" stop-color="#9c7a26"/>
        <stop offset="0.5" stop-color="#c4a148"/>
        <stop offset="1" stop-color="#a07e2a"/>
      </linearGradient>
    </defs>
    <path d="M0,245 C200,200 400,165 680,178 L680,389 L0,389 Z" fill="url(#goldBand)"/>
  </svg>

  <div class="wordmark">KORV Holdings</div>

  <div class="holder">
    <div class="holder__name">Damian Whitcombe</div>
    <div class="holder__role">IT &amp; Technical Support</div>
  </div>

  <div class="contact">
    <div class="contact__address">
      The Lumley House<br>
      12 Fenwick Lane<br>
      Ashcombe-Under-Lyne<br>
      Bristol, BS4 7QD
    </div>
    <div class="contact__row">
      <svg viewBox="0 0 12 12"><path d="M2 1h2.5l1 3-1.5 1a7 7 0 0 0 3 3l1-1.5 3 1V10a1 1 0 0 1-1 1C5 11 1 7 1 2a1 1 0 0 1 1-1z" fill="#fff"/></svg>
      <span>0845 20 73 410</span>
    </div>
    <div class="contact__row">
      <svg viewBox="0 0 12 12"><rect x="3" y="0.5" width="6" height="11" rx="1" fill="#fff"/><rect x="4" y="2" width="4" height="6" fill="#a8862e"/></svg>
      <span>07700 900 318</span>
    </div>
    <div class="contact__row">
      <svg viewBox="0 0 12 12"><rect x="1" y="4" width="10" height="6" rx="1" fill="#fff"/><rect x="3" y="1" width="6" height="3" fill="#fff"/></svg>
      <span>0845 20 73 510</span>
    </div>
    <div class="contact__row">
      <svg viewBox="0 0 12 12"><rect x="0.5" y="2" width="11" height="8" fill="#fff"/><path d="M0.5 2l5.5 4.5L11.5 2" fill="none" stroke="#a8862e" stroke-width="1"/></svg>
      <span>damian@korv.co</span>
    </div>
    <div class="contact__row">
      <svg viewBox="0 0 12 12"><path d="M6 1l5 5-5 5-1-1 3.2-3.3H1V5.3h7.2L5 2z" fill="#fff"/></svg>
      <span>www.korv.co</span>
    </div>
  </div>
</section>

</body>
</html>
```